Design clean technology service-based company website

Hello, We are looking to reskin our company website. We are an environmental inspection company and test for Asbestos, Lead and Mold along with other contaminants. People depend on the results to be accurate and fast. We are regulated by the NQB and State regulations. We work a lot with business to business and business to customer. We are wanting to make our new presentation to be modern and easy for customers to interact with us, understand our process and services while providing valuable environmental informational resource and updates. We are a technology based company and will be providing instantaneous results as reports come in for the customers. We are needing good calls to action on the site to direct them to setup a new inspection. Each user will have a backend access to their job information with invoices, reports, status, etc. We have developed software to be able to proved these reports and want to look the part.

My current website is www.trylumaverde.com
Updates

Helllo we are wanting to make sure we have good time to select the right website for us and also have the additional time to select other pages of the website. We have received great designs and have consolidated our requests into a document for the next set of iterations.

Target Market(s)

Home Owners, Contractors, Engineers, Real Estate Agents, Building Owners, Insurance Adjusters

Industry/Entity Type

Environmental Consultant

Number of Pages Required

5+ page

Font styles to use
Sans Serif

Colors
0355a3
9bcb3c
7f7f7f
f5f5f5
000000

Requirements
Must have
• Use our existing logo to design around
• The layouts look good in mobile mode for understanding and selecting services and signing up
• Clean Modern Layout
• Have all pages on the website have a similar layout and feel
• Clearly communicate services along with bundle service packages
• Detail the customer journey with graphic design
• Great call to actions to either schedule inspection online, call, text, chat
Nice to have
• Have an interactive graphic for where to test for lead, asbestos and mold.
• I like the becky barlows top order line bar - see attached
• Have clear question and answer page layouts for asbestos, lead and mold
• Show Company reviews
• Have clear Resources pages for all types of contaminants
Should not have
• My current website is www.trylumaverde.com

```html
<!DOCTYPE html>
<html lang="en">
<head>
<meta charset="utf-8">
<title>Lumaverde Environmental Inspections</title>
<link href="https://fonts.googleapis.com/css2?family=Open+Sans:wght@400;600;700&display=swap" rel="stylesheet">
<style>
:root{
  --blue:#0355a3;
  --blue-deep:#0a4a8c;
  --blue-footer:#0b3f78;
  --green:#9bcb3c;
  --grey:#7f7f7f;
  --grey-dark:#555;
  --light:#f5f5f5;
  --black:#000;
  --white:#fff;
}
*{box-sizing:border-box;margin:0;padding:0}
html,body{width:1200px;height:3214px;overflow:hidden;background:var(--white)}
body{font-family:"Open Sans",Arial,sans-serif;color:var(--grey)}
.page{position:relative;width:1200px;height:3214px;overflow:hidden}
.abs{position:absolute}

/* header */
.site-header{position:absolute;left:0;top:0;width:1200px;height:103px;background:var(--white)}
.brand{position:absolute;left:86px;top:30px;display:flex;align-items:center;gap:12px}
.brand-dot{width:22px;height:22px;border-radius:50%;background:var(--green)}
.brand-name{font-size:40px;font-weight:600;color:var(--green);line-height:1;letter-spacing:.5px}
.main-nav a{position:absolute;top:62px;font-size:14px;font-weight:600;color:#444;text-decoration:none;text-transform:uppercase;letter-spacing:.3px}
.main-nav a.active{color:var(--green)}

/* hero */
.hero{position:absolute;left:0;top:103px;width:1200px;height:497px;background:linear-gradient(100deg,#d7d4cf 0%,#bdb7ae 22%,#6b6258 34%,#a8a198 48%,#cfcbc4 70%,#dcd9d4 100%)}
.hero-person{position:absolute;left:890px;top:28px;width:278px;height:469px;background:linear-gradient(180deg,#e9953a 0%,#d65a3a 28%,#2f6fb5 60%,#27497a 100%);border-radius:120px 120px 0 0}
.hero-title{position:absolute;left:0;width:1230px;top:150px;text-align:center;font-size:40px;font-weight:700;color:var(--green);letter-spacing:.5px}
.hero-sub{position:absolute;left:270px;width:690px;top:210px;text-align:center;font-size:28px;line-height:36px;color:var(--white);text-shadow:0 1px 3px rgba(0,0,0,.35)}
.btn-hero{position:absolute;left:501px;top:311px;width:159px;height:40px;border-radius:6px;background:var(--blue);color:var(--white);font-size:18px;font-weight:700;line-height:40px;text-align:center}
.hero-dots{position:absolute;left:554px;top:388px;display:flex;gap:8px}
.hero-dots span{width:11px;height:11px;border-radius:50%;border:2px solid var(--white)}
.hero-dots span.on{background:var(--green);border-color:var(--green)}

/* accreditation band */
.accreditations{position:absolute;left:0;top:600px;width:1200px;height:116px;background:var(--green)}
.badge{position:absolute;background:var(--white);opacity:.95}

/* section titles */
.section-title{position:absolute;left:0;width:1200px;text-align:center;font-size:32px;font-weight:700;color:var(--grey-dark)}
.about-text{position:absolute;left:196px;width:808px;top:800px;text-align:center;font-size:15px;line-height:26px;color:var(--grey)}

/* services */
.service{position:absolute;top:1008px;width:220px;text-align:center}
.service-icon{display:block;margin:0 auto}
.service-name{margin-top:28px;font-size:16px;font-weight:600;color:#444}
.service-text{margin-top:8px;font-size:12px;line-height:21px;color:var(--grey);text-align:justify;padding:0 12px}
.service-divider{position:absolute;top:1000px;width:1px;height:190px;background:#ddd}

/* journey */
.journey-title{position:absolute;left:86px;top:1260px;font-size:32px;font-weight:700;color:var(--grey-dark)}
.journey-text{position:absolute;left:86px;top:1322px;width:666px;font-size:13px;line-height:24px;color:var(--grey)}
.journey-diagram{position:absolute;left:86px;top:1426px}
.journey-laptop{position:absolute;left:504px;top:1603px;width:248px;height:122px;background:linear-gradient(180deg,#3a3a3a 0%,#e9eef2 8%,#dfe8ee 86%,#444 87%,#777 100%);border-radius:6px}
.journey-person{position:absolute;left:793px;top:1307px;width:321px;height:489px;background:linear-gradient(180deg,#f4cc1a 0%,#e4b98f 24%,#eef1f6 42%,#dde3ec 100%);border-radius:150px 150px 0 0}

/* call band */
.call-band{position:absolute;left:0;top:1796px;width:1200px;height:128px;background:var(--blue)}
.call-line{position:absolute;left:0;width:1200px;top:22px;text-align:center;font-size:24px;color:var(--white)}
.call-line:before,.call-line:after{content:"";display:inline-block;width:34px;height:2px;background:var(--white);vertical-align:middle;margin:0 20px}
.call-phone{position:absolute;left:0;width:1200px;top:68px;text-align:center;font-size:22px;color:var(--white)}
.call-note{position:absolute;left:0;width:1200px;top:98px;text-align:center;font-size:10px;color:var(--white)}

/* work areas */
.work-areas{position:absolute;left:0;top:1924px;width:1200px;height:562px;background:var(--light)}
.work-card{position:absolute;top:129px;width:231px;height:386px;background:var(--white);box-shadow:0 2px 8px rgba(0,0,0,.18)}
.work-photo{width:231px;height:163px}
.work-name{margin:10px 0 0 28px;font-size:16px;line-height:20px;color:var(--green)}
.work-text{margin:10px 24px 0 28px;font-size:12px;line-height:22px;color:var(--grey)}
.btn-view{position:absolute;left:28px;bottom:26px;width:80px;height:30px;border-radius:15px;box-shadow:0 1px 5px rgba(0,0,0,.2);font-size:10px;line-height:30px;text-align:center;color:var(--green)}
.slide-arrow{position:absolute;top:303px;width:34px;height:34px;border-radius:50%;background:var(--green)}

/* testimonial */
.testimonial{position:absolute;left:0;top:2486px;width:1200px;height:294px;background:linear-gradient(100deg,#2b3747 0%,#46505c 40%,#2a3442 100%)}
.quote-mark{position:absolute;left:0;width:1200px;top:20px;text-align:center;font-size:64px;font-weight:700;color:var(--white);line-height:1}
.quote-text{position:absolute;left:200px;width:800px;top:88px;text-align:center;font-size:14px;line-height:24px;color:var(--white)}
.quote-name{position:absolute;left:0;width:1200px;top:178px;text-align:center;font-size:13px;font-weight:700;color:var(--white)}
.quote-role{position:absolute;left:0;width:1200px;top:198px;text-align:center;font-size:11px;color:#d8d8d8}
.quote-dots{position:absolute;left:590px;top:234px;display:flex;gap:5px}
.quote-dots span{width:7px;height:7px;border-radius:50%;border:1px solid #ccc}
.quote-dots span.on{background:var(--green);border-color:var(--green)}

/* enquire */
.enquire{position:absolute;left:0;top:2780px;width:1200px;height:257px;background:var(--blue)}
.enquire-title{position:absolute;left:0;width:1200px;top:30px;text-align:center;font-size:30px;font-weight:700;color:var(--white)}
.field{position:absolute;top:98px;width:245px;height:50px;background:#e8eef6;color:#9aa;font-size:13px;line-height:50px;padding-left:14px}
.btn-enquire{position:absolute;left:759px;top:98px;width:244px;height:50px;border:1px solid var(--white);color:var(--white);font-size:13px;font-weight:600;line-height:48px;text-align:center}
.enquire-note{position:absolute;left:0;width:1200px;top:183px;text-align:center;font-size:11px;color:var(--white)}

/* footer */
.site-footer{position:absolute;left:0;top:3037px;width:1200px;height:152px;background:var(--blue-footer)}
.foot-col{position:absolute;top:30px}
.foot-col svg{position:absolute;left:0;top:0}
.foot-head{margin-left:42px;font-size:15px;font-weight:600;color:var(--white)}
.foot-body{margin:8px 0 0 42px;font-size:12px;line-height:20px;color:#d6e2f0}
.copyright{position:absolute;left:0;top:3189px;width:1200px;height:25px;background:#083262;text-align:center;font-size:10px;line-height:25px;color:#c8d4e2}
</style>
</head>
<body>
<div class="page">

  <header class="site-header">
    <div class="brand"><span class="brand-dot"></span><span class="brand-name">lumaverde</span></div>
    <nav class="main-nav">
      <a class="active" style="left:430px">Home</a>
      <a style="left:526px">Our Services</a>
      <a style="left:684px">Resources</a>
      <a style="left:811px">Blog</a>
      <a style="left:907px">Reviews</a>
      <a style="left:1034px">Connect</a>
    </nav>
  </header>

  <section class="hero" role="img" aria-label="Mold-stained wall with power socket and cleaning supplies">
    <div class="hero-person" role="img" aria-label="Inspector in hard hat and overalls writing on a clipboard"></div>
    <h1 class="hero-title">LOREM IPSUM</h1>
    <p class="hero-sub">Lorem Ipsum Dolar Sit Amit Lorem Ipsum Dolar Sit Amit Lorem Ipsum Dolar Sit Amit</p>
    <div class="btn-hero">Know More</div>
    <div class="hero-dots"><span class="on"></span><span></span><span></span></div>
  </section>

  <section class="accreditations" aria-label="Accreditations">
    <div class="badge" style="left:86px;top:24px;width:150px;height:56px;border-radius:6px" role="img" aria-label="Accredited business badge"></div>
    <div class="badge" style="left:315px;top:24px;width:146px;height:56px;border-radius:6px" role="img" aria-label="NQB badge"></div>
    <div class="badge" style="left:516px;top:22px;width:62px;height:62px;border-radius:50%" role="img" aria-label="Certification badge"></div>
    <div class="badge" style="left:739px;top:22px;width:70px;height:70px;border-radius:50%" role="img" aria-label="Association seal"></div>
    <div class="badge" style="left:881px;top:24px;width:233px;height:56px;border-radius:6px" role="img" aria-label="State health department badge"></div>
  </section>

  <h2 class="section-title" style="top:738px">About us</h2>
  <p class="about-text">Lumaverde grew up in the rough and tumble disaster restoration industry. Time and time again, we saw projects small and large brought to a stand-still to await environmental testing and results.Lumaverde grew up in the rough and tumble disaster restoration industry. Time and time again, we saw projects small and large brought to a stand-still to await environmental testing and results.</p>

  <h2 class="section-title" style="top:926px">Our Services</h2>
  <div class="service-divider" style="left:370px"></div>
  <div class="service-divider" style="left:595px"></div>
  <div class="service-divider" style="left:820px"></div>

  <div class="service" style="left:149px">
    <svg class="service-icon" width="72" height="72" viewBox="0 0 72 72"><circle cx="36" cy="36" r="34" fill="none" stroke="var(--blue)" stroke-width="2"/><path d="M26 34h6v14h-6z M34 34l6-10c2 0 3 1 3 3l-1 6h7c2 0 3 2 2 4l-3 9c-1 2-2 2-3 2H34z" fill="var(--blue)"/></svg>
    <div class="service-name">Lead Inspection</div>
    <p class="service-text">Lorem Ipsum is simply dummy text of the printing and typesetting industry.</p>
  </div>
  <div class="service" style="left:372px">
    <svg class="service-icon" width="72" height="72" viewBox="0 0 72 72"><circle cx="36" cy="36" r="34" fill="none" stroke="var(--blue)" stroke-width="2"/><circle cx="36" cy="28" r="6" fill="var(--blue)"/><circle cx="24" cy="31" r="5" fill="var(--blue)"/><circle cx="48" cy="31" r="5" fill="var(--blue)"/><path d="M26 48c0-7 4-11 10-11s10 4 10 11z M15 46c0-5 3-8 9-8 2 0 3 1 3 1-2 2-3 4-3 7z M57 46c0-5-3-8-9-8-2 0-3 1-3 1 2 2 3 4 3 7z" fill="var(--blue)"/></svg>
    <div class="service-name">Mold Inspection</div>
    <p class="service-text">Lorem Ipsum is simply dummy text of the printing and typesetting industry.</p>
  </div>
  <div class="service" style="left:597px">
    <svg class="service-icon" width="72" height="72" viewBox="0 0 72 72"><circle cx="36" cy="36" r="34" fill="none" stroke="var(--blue)" stroke-width="2"/><rect x="25" y="22" width="3" height="30" fill="var(--blue)"/><path d="M28 23c6-3 10 3 18 0v14c-8 3-12-3-18 0z" fill="var(--blue)"/></svg>
    <div class="service-name">Asbestos Inspection</div>
    <p class="service-text">Lorem Ipsum is simply dummy text of the printing and typesetting industry.</p>
  </div>
  <div class="service" style="left:816px">
    <svg class="service-icon" width="72" height="72" viewBox="0 0 72 72"><circle cx="36" cy="36" r="34" fill="none" stroke="var(--blue)" stroke-width="2"/><rect x="21" y="26" width="30" height="21" rx="3" fill="var(--blue)"/><rect x="21" y="31" width="30" height="4" fill="var(--white)"/><rect x="25" y="40" width="9" height="3" fill="var(--white)"/></svg>
    <div class="service-name">Pricing</div>
    <p class="service-text">Lorem Ipsum is simply dummy text of the printing and typesetting industry.</p>
  </div>

  <h2 class="journey-title">Customers Journey With us . . !</h2>
  <p class="journey-text">First, we had to know when it's prudent or even required by law to test for asbestos, lead-based paint, mold or other contaminants. Then we had to track down reliable testing companies, faciliti we had to ensure we safeguarded people and property i</p>

  <svg class="journey-diagram" width="690" height="335" viewBox="0 0 690 335" font-family="Open Sans, Arial, sans-serif">
    <rect x="4" y="14" width="680" height="316" fill="none" stroke="#d0d0d0" stroke-width="1.5"/>
    <polygon points="18,8 150,8 162,21 150,34 18,34" fill="var(--blue)"/>
    <polygon points="150,8 288,8 300,21 288,34 150,34 162,21" fill="var(--green)"/>
    <polygon points="288,8 426,8 438,21 426,34 288,34 300,21" fill="var(--grey)"/>
    <polygon points="426,8 552,8 564,21 552,34 426,34 438,21" fill="var(--blue)"/>
    <polygon points="552,8 664,8 676,21 664,34 552,34 564,21" fill="var(--green)"/>
    <g fill="#fff" font-size="11" font-weight="600" text-anchor="middle">
      <text x="82" y="25">Discovery</text><text x="222" y="25">Requirement</text><text x="360" y="25">Inspection</text><text x="492" y="25">Statistics</text><text x="612" y="25">Reports</text>
    </g>
    <path d="M222 34v22 M68 56h270 M68 56v23 M158 56v23 M246 56v23 M336 56v23" stroke="#999" stroke-width="1.5" fill="none"/>
    <g fill="var(--blue)">
      <circle cx="68" cy="117" r="28"/><circle cx="158" cy="117" r="28"/><circle cx="246" cy="117" r="28"/><circle cx="336" cy="117" r="28"/>
    </g>
    <g fill="#999"><path d="M108 113l8 4-8 4z"/><path d="M198 113l8 4-8 4z"/><path d="M286 113l8 4-8 4z"/></g>
    <g stroke="#fff" stroke-width="2.5" fill="none">
      <circle cx="68" cy="117" r="11"/><circle cx="68" cy="117" r="4"/>
      <rect x="150" y="106" width="16" height="21" rx="2"/><path d="M154 113h8 M154 119h8"/>
      <circle cx="246" cy="112" r="5"/><path d="M237 128c1-6 4-9 9-9s8 3 9 9"/>
      <circle cx="336" cy="117" r="11"/><path d="M336 110v7l5 4"/>
    </g>
    <g fill="#333" font-size="11" font-weight="600" text-anchor="middle">
      <text x="68" y="163">Goals</text><text x="158" y="163">Content</text><text x="246" y="163">Experience</text><text x="336" y="163">Schedule</text>
    </g>
    <g fill="var(--green)"><path d="M60 189l8-7 8 7z"/><path d="M150 189l8-7 8 7z"/><path d="M238 189l8-7 8 7z"/><path d="M328 189l8-7 8 7z"/></g>
    <g fill="var(--green)">
      <circle cx="68" cy="237" r="28"/><circle cx="158" cy="237" r="28"/><circle cx="246" cy="237" r="28"/><circle cx="336" cy="237" r="28"/>
    </g>
    <g fill="#3b3b3b">
      <path d="M58 244l10-17 10 17z"/>
      <path d="M150 226h10v14h-10z M160 232l8-3v14l-8-3z"/>
      <path d="M246 224l4 9 10 1-8 6 3 10-9-6-9 6 3-10-8-6 10-1z" fill="none" stroke="#3b3b3b" stroke-width="2"/>
      <ellipse cx="336" cy="237" rx="13" ry="8" fill="none" stroke="#3b3b3b" stroke-width="2.5"/><circle cx="336" cy="237" r="4"/>
    </g>
    <g fill="#333" font-size="11" font-weight="600" text-anchor="middle">
      <text x="68" y="281">Customer</text><text x="68" y="294">Value</text>
      <text x="158" y="281">Customer</text><text x="158" y="294">Retention</text>
      <text x="246" y="281">Customer</text><text x="246" y="294">Satisfaction</text>
      <text x="336" y="281">Brand</text><text x="336" y="294">Awareness</text>
    </g>
  </svg>
  <div class="journey-laptop" role="img" aria-label="Laptop showing a customer job status dashboard"></div>
  <div class="journey-person" role="img" aria-label="Smiling inspector in a yellow hard hat with arms crossed"></div>

  <section class="call-band">
    <div class="call-line">Call us to get Instant Help &amp; talk to one of our Team</div>
    <div class="call-phone">(555) 210-4478</div>
    <div class="call-note">our times are open mon - sat</div>
  </section>

  <section class="work-areas">
    <h2 class="section-title" style="top:44px">Our Work Areas</h2>
    <div class="slide-arrow" style="left:146px"><svg width="34" height="34" viewBox="0 0 34 34"><path d="M19 11l-6 6 6 6" stroke="#fff" stroke-width="3" fill="none"/></svg></div>
    <div class="slide-arrow" style="left:1027px"><svg width="34" height="34" viewBox="0 0 34 34"><path d="M15 11l6 6-6 6" stroke="#fff" stroke-width="3" fill="none"/></svg></div>

    <article class="work-card" style="left:221px">
      <div class="work-photo" role="img" aria-label="Asbestos fibres with a protective dust mask" style="background:linear-gradient(160deg,#4a4a4a,#bdbdbd 55%,#e6e6e6)"></div>
      <h3 class="work-name">Asbestos<br>Inspections</h3>
      <p class="work-text">At Lumaverde, we are experienced in assessing the environmental hazards that merit or even require</p>
      <div class="btn-view">View More</div>
    </article>
    <article class="work-card" style="left:491px">
      <div class="work-photo" role="img" aria-label="Lead test samples being handled in a lab" style="background:linear-gradient(160deg,#2e2e2e,#8a8a7a 50%,#c9c2a0)"></div>
      <h3 class="work-name">Lead<br>Inspections</h3>
      <p class="work-text">We are trained and certified to safely obtain environmental test samples environmental test samples</p>
      <div class="btn-view">View More</div>
    </article>
    <article class="work-card" style="left:761px">
      <div class="work-photo" role="img" aria-label="Worker in protective suit spraying mold remediation" style="background:linear-gradient(160deg,#e2e2e0,#c8c6c0 50%,#a9a49a)"></div>
      <h3 class="work-name">Mold<br>Inspactions</h3>
      <p class="work-text">working relationship with top-rated testing facilities that enable us to get most test results .</p>
      <div class="btn-view">View More</div>
    </article>
  </section>

  <section class="testimonial" role="img" aria-label="Dark photo of a hand writing with a pen">
    <div class="quote-mark">&rdquo;</div>
    <p class="quote-text">" Lorem Ipsum is simply dummy text of the printing and typesetting industry. Lorem Ipsum has been the industry's standard dummy text ever since the 1500s, when an unknown printer took a galley of type and scrambled it to make a type specimen book..! "</p>
    <div class="quote-name">LOREM IPSUM</div>
    <div class="quote-role">Manager</div>
    <div class="quote-dots"><span class="on"></span><span></span><span></span></div>
  </section>

  <section class="enquire">
    <h2 class="enquire-title">Enquire With us</h2>
    <div class="field" style="left:206px">Name</div>
    <div class="field" style="left:484px">Message</div>
    <div class="btn-enquire">Enquire Now</div>
    <p class="enquire-note">Please Contact us if you have any query Regarding Environmental Inspections</p>
  </section>

  <footer class="site-footer">
    <div class="foot-col" style="left:94px">
      <svg width="26" height="26" viewBox="0 0 26 26"><circle cx="13" cy="13" r="12" fill="none" stroke="#fff" stroke-width="1.5"/><path d="M13 6c-3 0-5 2-5 5 0 4 5 9 5 9s5-5 5-9c0-3-2-5-5-5z" fill="#fff"/><circle cx="13" cy="11" r="2" fill="var(--blue-footer)"/></svg>
      <div class="foot-head">Our Address</div>
      <div class="foot-body">Door No, Street No,<br>City, State, Country</div>
    </div>
    <div class="foot-col" style="left:516px">
      <svg width="26" height="26" viewBox="0 0 26 26"><circle cx="13" cy="13" r="12" fill="none" stroke="#fff" stroke-width="1.5"/><path d="M9 7l3 3-2 2c1 2 2 3 4 4l2-2 3 3-2 2c-5 0-10-5-10-10z" fill="#fff"/></svg>
      <div class="foot-head">Contact Us</div>
      <div class="foot-body">0(123)-456789,<br>0(123)-456789,<br>info@companyname.com</div>
    </div>
    <div class="foot-col" style="left:866px">
      <svg width="26" height="26" viewBox="0 0 26 26"><circle cx="13" cy="13" r="12" fill="none" stroke="#fff" stroke-width="1.5"/><path d="M13 7v6l4 3" stroke="#fff" stroke-width="2" fill="none"/></svg>
      <div class="foot-head">Our Timings</div>
      <div class="foot-body">Mon - Fri : 10am to 6pm<br>Sat - 10am to 2pm,<br>Sun - Holiday</div>
    </div>
  </footer>
  <div class="copyright">Copyrights Reserved @2017 Lumaverde</div>

</div>
</body>
</html>
```